" Atendimento médico em consultório/Clinica para mulheres em geral. A clinica contará com três médicas ginecologistas. Inicialmente somente a Dra. Lívia atenderá. O principal valor da Clinica é com o cuidado com a Mulher através de atendimento individual e cuidadoso através de especialistas nas áreas da ginecologia e Obstetricia. Apesar de possuir atendimento Obstétrico, o mesmo não será o principal foco da clinica. "

```html
<!DOCTYPE html>
<html lang="pt-BR">
<head>
<meta charset="utf-8">
<title>Ginecologia Alvorada — Cartão de visita</title>
<link rel="stylesheet" href="https://fonts.googleapis.com/css2?family=Cormorant+Garamond:wght@400;500&family=Roboto:wght@400;700&display=swap">
<style>
  :root {
    --page: #e9e9eb;
    --card: #ffffff;
    --rose: #e0727a;
    --rose-soft: #f4cfd1;
    --rose-faint: #fbeced;
    --ink: #2b2b2b;
    --gray: #8a8a8a;
  }
  * { margin: 0; padding: 0; box-sizing: border-box; }
  html, body { width: 1200px; height: 1200px; overflow: hidden; }
  body {
    background: var(--page);
    font-family: "Roboto", Arial, sans-serif;
    position: relative;
  }
  .card {
    position: absolute;
    left: 120px;
    width: 960px;
    height: 530px;
    background: var(--card);
    border-radius: 34px;
    overflow: hidden;
    box-shadow: 0 6px 24px rgba(0,0,0,0.12);
  }
  .card--front { top: 45px; }
  .card--back { top: 625px; }

  .card__band {
    position: absolute; left: 0; right: 0; bottom: 0; height: 44px;
    background: var(--rose);
  }
  .card__band-line {
    position: absolute; left: 0; right: 0; bottom: 54px; height: 4px;
    background: var(--rose);
  }
  .card__watermark {
    position: absolute; border-radius: 50%;
    background: radial-gradient(circle, var(--rose-faint) 0%, rgba(251,236,237,0) 70%);
  }
  .card--front .card__watermark { width: 560px; height: 560px; left: -120px; top: -140px; }
  .card--back .card__watermark { width: 600px; height: 600px; left: 330px; top: -40px; }

  .brand-mark {
    position: absolute; border-radius: 50%;
    border: 3px solid var(--rose);
    background: var(--rose-faint);
  }
  .brand-name {
    font-family: "Cormorant Garamond", Georgia, serif;
    font-weight: 500;
    color: var(--rose);
    position: absolute;
    white-space: nowrap;
  }

  /* Front */
  .card--front .brand-mark { width: 110px; height: 110px; left: 425px; top: 95px; }
  .card--front .brand-name { font-size: 76px; left: 0; right: 0; text-align: center; top: 215px; }
  .doctor-name {
    position: absolute; left: 0; right: 0; top: 315px; text-align: center;
    font-family: "Cormorant Garamond", Georgia, serif;
    font-size: 34px; color: var(--gray); letter-spacing: 0.5px;
  }

  /* Back */
  .card--back .brand-mark { width: 120px; height: 120px; left: 190px; top: 110px; }
  .card--back .brand-name { font-size: 40px; left: 90px; width: 320px; text-align: center; top: 250px; }
  .person {
    position: absolute; right: 70px; top: 80px; text-align: right;
    padding-right: 18px; border-right: 5px solid var(--rose);
  }
  .person__name { font-weight: 700; font-size: 34px; color: var(--ink); line-height: 1.1; }
  .person__role { font-size: 20px; color: var(--gray); margin-top: 2px; }
  .contacts {
    position: absolute; right: 70px; top: 190px; list-style: none;
  }
  .contacts li {
    display: flex; align-items: center; justify-content: flex-end; gap: 14px;
    font-size: 17px; color: var(--gray); line-height: 1.25; margin-bottom: 12px; text-align: right;
  }
  .contacts svg { width: 30px; height: 30px; flex: none; }
</style>
</head>
<body>

<section class="card card--front" aria-label="Frente do cartão">
  <div class="card__watermark" role="img" aria-label="Marca da clínica em tom claro ao fundo"></div>
  <div class="brand-mark" aria-hidden="true"></div>
  <p class="brand-name">Ginecologia Alvorada</p>
  <p class="doctor-name">Dra. Lívia Moraes Teixeira</p>
  <div class="card__band-line"></div>
  <div class="card__band"></div>
</section>

<section class="card card--back" aria-label="Verso do cartão">
  <div class="card__watermark" role="img" aria-label="Marca da clínica em tom claro ao fundo"></div>
  <div class="brand-mark" aria-hidden="true"></div>
  <p class="brand-name">Ginecologia Alvorada</p>

  <div class="person">
    <p class="person__name">Nome Completo</p>
    <p class="person__role">Cargo</p>
  </div>

  <ul class="contacts">
    <li><span>(xx) xxxx-xxxx<br>(xx) xxxx-xxxx</span>
      <svg viewBox="0 0 30 30"><circle cx="15" cy="15" r="14" fill="var(--rose)"/><path d="M10 8c1 0 2 2 2.5 3.5.3 1-1.2 1.5-.8 2.5.8 2 2.3 3.5 4.3 4.3 1 .4 1.5-1.1 2.5-.8C20 18 22 19 22 20c0 1.5-1.5 2.5-3 2.5C13 22.5 7.5 17 7.5 11 7.5 9.5 8.5 8 10 8z" fill="#fff"/></svg></li>
    <li><span>R. Seu Endereço<br>Cidade-Estado<br>CEP 00000-000</span>
      <svg viewBox="0 0 30 30"><circle cx="15" cy="15" r="14" fill="var(--rose)"/><path d="M15 7a5.5 5.5 0 0 0-5.5 5.5C9.5 17 15 23 15 23s5.5-6 5.5-10.5A5.5 5.5 0 0 0 15 7z" fill="#fff"/><circle cx="15" cy="12.5" r="2" fill="var(--rose)"/></svg></li>
    <li><span>contato@alvorada.med</span>
      <svg viewBox="0 0 30 30"><circle cx="15" cy="15" r="14" fill="var(--rose)"/><rect x="8" y="10" width="14" height="10" rx="1" fill="#fff"/><path d="M8.5 10.5 15 15.5l6.5-5" stroke="var(--rose)" stroke-width="1.4" fill="none"/></svg></li>
    <li><span>Rede social</span>
      <svg viewBox="0 0 30 30"><circle cx="15" cy="15" r="14" fill="var(--rose)"/><circle cx="15" cy="15" r="5" fill="#fff"/></svg></li>
  </ul>

  <div class="card__band-line"></div>
  <div class="card__band"></div>
</section>

</body>
</html>
```